Business Card Design Project

We need a buisness card for a new digital sinage company. Our target cliants are small to mediaum buisness who want to advertise on out digital sinage network

Target Market(s)

Small to medium buisness

Industry/Entity Type

Digital

Requirements
Must have
• Must have logo

```html
<!DOCTYPE html>
<html lang="en">
<head>
<meta charset="utf-8">
<title>Signo Business Card</title>
<link href="https://fonts.googleapis.com/css2?family=Montserrat:wght@400;500;700;900&display=swap" rel="stylesheet">
<style>
  :root {
    --backdrop: #e6e2df;
    --card-white: #fbfbfb;
    --card-black: #050505;
    --ink: #111111;
    --ink-soft: #2b2b2b;
    --accent-orange: #f39200;
    --accent-blue: #1d9bd8;
    --band-light: #ececec;
    --band-dark: #262626;
    --paper-white: #ffffff;
  }
  * { box-sizing: border-box; margin: 0; padding: 0; }
  html, body {
    width: 1200px;
    height: 900px;
    overflow: hidden;
    background: var(--backdrop);
    font-family: "Montserrat", Arial, sans-serif;
  }
  .canvas {
    width: 1200px;
    height: 900px;
    display: flex;
    flex-direction: column;
    align-items: center;
    justify-content: center;
    gap: 40px;
  }
  .card {
    position: relative;
    width: 660px;
    height: 377px;
    overflow: hidden;
    box-shadow: 0 6px 18px rgba(0,0,0,0.18);
  }
  .card--front { background: var(--card-white); }
  .card--back { background: var(--card-black); }

  .band { position: absolute; height: 34px; }
  .card--front .band { background: var(--band-light); left: 0; width: 300px; }
  .card--front .band--top { top: 52px; }
  .card--front .band--bottom { top: 238px; }
  .card--back .band { background: var(--band-dark); }
  .card--back .band--left { left: 0; width: 148px; }
  .card--back .band--right { right: 0; width: 166px; }
  .band--left.band--1 { top: 168px; }
  .band--left.band--2 { top: 210px; }
  .band--left.band--3 { top: 252px; }
  .band--right.band--1 { top: 40px; }
  .band--right.band--2 { top: 82px; }
  .band--right.band--3 { top: 124px; }

  .brand {
    position: absolute;
    display: flex;
    align-items: center;
    font-weight: 900;
    letter-spacing: -1px;
    line-height: 1;
    white-space: nowrap;
  }
  .brand__square {
    display: block;
    flex: none;
    background: var(--accent-blue);
    border-radius: 6px;
  }
  .card--front .brand { left: 42px; top: 122px; gap: 14px; font-size: 50px; color: var(--ink); }
  .card--front .brand__square { width: 62px; height: 62px; }
  .card--back .brand {
    left: 166px; top: 136px;
    gap: 18px; font-size: 56px; color: var(--paper-white);
  }
  .card--back .brand__square { width: 100px; height: 100px; border-radius: 8px; }

  .contact {
    position: absolute;
    right: 38px;
    top: 108px;
    text-align: right;
    color: var(--ink-soft);
  }
  .contact__name { font-size: 24px; font-weight: 900; color: var(--ink); letter-spacing: 0.3px; }
  .contact__title { font-size: 14px; font-weight: 500; color: var(--accent-orange); letter-spacing: 2px; margin-bottom: 16px; }
  .contact__line { font-size: 14px; font-weight: 400; letter-spacing: 1.4px; line-height: 1.4; }
  .contact__web { font-size: 16px; font-weight: 700; color: var(--accent-orange); letter-spacing: 1.4px; margin-top: 10px; }
</style>
</head>
<body>
<main class="canvas">
  <section class="card card--front" aria-label="Business card front">
    <div class="band band--top"></div>
    <div class="band band--bottom"></div>
    <div class="brand"><span class="brand__square"></span>Signo</div>
    <div class="contact">
      <p class="contact__name">Jordan Pell</p>
      <p class="contact__title">MANAGER DIRECTOR</p>
      <p class="contact__line">jordan@signodisplay.com.au</p>
      <p class="contact__line">0412345678</p>
      <p class="contact__line">PO Box 142 Harbour Point</p>
      <p class="contact__line">WA 6700</p>
      <p class="contact__web">www.signodisplay.com.au</p>
    </div>
  </section>

  <section class="card card--back" aria-label="Business card back">
    <div class="band band--left band--1"></div>
    <div class="band band--left band--2"></div>
    <div class="band band--left band--3"></div>
    <div class="band band--right band--1"></div>
    <div class="band band--right band--2"></div>
    <div class="band band--right band--3"></div>
    <div class="brand"><span class="brand__square"></span>Signo</div>
  </section>
</main>
</body>
</html>
```